Organic skincare label - minimalist, earthy, luxe design needed!

I need a label design for a luxury natural skin care line called "Velka Botanix". Velka means 'earth' in Swahili. I would like the design to embody an earthy feel but be minimalistic and give a luxe vibe. My first product will be a Tumeric and Neem Scrub.

The size of the jar is 8oz, label dimensions should be (1.625" Tall x 8.5" Wide)
I will be making other products too such as; oils + toners so I feel free to do labels for glass bottles and/or spray bottles as well.

Forest green, light pinks/nudes/beige, grey, white, gold, are colors that can be used (not all have to be used).

I have included pictures of some things I've worked on myself as well as my original logo design but I need to simplify the logo, no circle around it.
Feel free to get creative.

Thank you! :)
Updates

Target Market(s)

Socially Conscious, Beauty Enthusiast, Minimalist

Industry/Entity Type

Skin Care

Font styles to use
Sans Serif
Other font styles liked:
• "Wonderlove doodle" is the font used for "Velka" in the logo. Feel free to use that or change it as you see fit.

Requirements
Must have
• Simplistic design
would like to stick to a font close to the ones in the logo. Either the one used for the name "Velka" OR the one that the slogan "Rooted Rituals" uses.

I have also included some pictures to capture the aesthetic of my social media and website.

Gender neutral

```html
<!DOCTYPE html>
<html lang="en">
<head>
<meta charset="utf-8">
<title>Velka Botanix – Tumeric and Neem Scrub Labels</title>
<link rel="stylesheet" href="https://fonts.googleapis.com/css2?family=Poppins:wght@400;500;600&display=swap">
<style>
  :root {
    --backdrop: #d9d9d9;
    --label-olive: #1f2314;
    --copper: #b87a4e;
    --ivory: #f4f1ea;
  }
  * { margin: 0; padding: 0; box-sizing: border-box; }
  html, body {
    width: 1200px;
    height: 1200px;
    overflow: hidden;
    background: var(--backdrop);
  }
  .label-sheet {
    position: relative;
    width: 1200px;
    height: 1200px;
    font-family: "Poppins", sans-serif;
  }
  .label {
    position: absolute;
    top: 369px;
    height: 462px;
    background: var(--label-olive);
    color: var(--ivory);
    display: flex;
    flex-direction: column;
    align-items: center;
    text-align: center;
  }
  .label--wide { left: 33px; width: 704px; }
  .label--square { left: 781px; width: 386px; }

  .product-name {
    margin-top: 30px;
    font-size: 22px;
    font-weight: 400;
    white-space: nowrap;
  }
  .label--square .product-name { font-size: 18px; margin-top: 32px; }

  .wordmark {
    margin-top: 62px;
    font-size: 68px;
    line-height: 1;
    font-weight: 600;
    color: var(--copper);
    letter-spacing: 1px;
  }
  .label--square .wordmark { margin-top: 64px; font-size: 58px; }

  .tagline {
    margin-top: 10px;
    font-size: 20px;
    font-weight: 500;
    letter-spacing: 1px;
    color: var(--copper);
    white-space: nowrap;
  }
  .label--square .tagline { font-size: 17px; margin-top: 8px; }

  .ingredients {
    margin-top: 54px;
    font-size: 17.5px;
    line-height: 1.4;
    font-weight: 500;
    white-space: nowrap;
  }
  .label--square .ingredients { margin-top: 42px; font-size: 17px; }

  .net-volume {
    margin-top: 26px;
    font-size: 13px;
    font-weight: 600;
    color: var(--copper);
  }
  .label--square .net-volume { margin-top: 14px; }

  .origin {
    margin-top: 14px;
    font-size: 12.5px;
    font-weight: 600;
    white-space: nowrap;
  }
</style>
</head>
<body>
<main class="label-sheet">
  <section class="label label--wide" aria-label="Jar label, wide format">
    <h1 class="product-name">Tumeric and Neem Scrub</h1>
    <p class="wordmark">Velka</p>
    <p class="tagline">ROOTED RITUALS</p>
    <p class="ingredients">Ingredients Organic Rosehip Seed Oil, Organic Camelia Seed<br>Oil, Organic Pomegranate Oil, VitaminE non-GMO</p>
    <p class="net-volume">8oz / 59ml</p>
    <p class="origin">MADE IN ASHFORD, TX</p>
  </section>

  <section class="label label--square" aria-label="Bottle label, compact format">
    <h2 class="product-name">Tumeric and Neem Scrub</h2>
    <p class="wordmark">Velka</p>
    <p class="tagline">ROOTED RITUALS</p>
    <p class="ingredients">Ingredients Organic Rosehip<br>Seed Oil, Organic Camelia Seed<br>Oil, Organic Pomegranate<br>Oil, VitaminE non-GMO</p>
    <p class="net-volume">8oz / 59ml</p>
    <p class="origin">MADE IN ASHFORD, TX</p>
  </section>
</main>
</body>
</html>
```